Business cards and stationary for Auto Body Shop
R & T Auto Body Service Inc.
Simple
Delmor Quenivash
28476 Pellway Street
Corvale, CA 90999
rtautobodyinc@brivomail.com
www.rtautobody-example.com
Just the Logo I guess.
Please us this new logo.

```html
<!DOCTYPE html>
<html lang="en">
<head>
<meta charset="utf-8">
<title>R &amp; T Auto Body – Business Card</title>
<link rel="stylesheet" href="https://fonts.googleapis.com/css2?family=Cinzel:wght@400;600&display=swap">
<style>
  :root {
    --page-bg: #e9e6e1;
    --card-black: #0b0b0b;
    --card-black-soft: #1a1a1a;
    --brand-red: #d3141c;
    --band-red: #c8111a;
    --band-edge: #7d0a0f;
    --text-light: #ececec;
    --text-muted: #c9c9c9;
  }
  html, body {
    margin: 0;
    padding: 0;
    width: 1200px;
    height: 914px;
    overflow: hidden;
    background: var(--page-bg);
  }
  .canvas {
    position: relative;
    width: 1200px;
    height: 914px;
  }
  .business-card {
    position: absolute;
    left: 75px;
    top: 157px;
    width: 1050px;
    height: 600px;
    background: radial-gradient(ellipse at 40% 35%, var(--card-black-soft), var(--card-black) 70%);
    box-shadow: 0 10px 30px rgba(0,0,0,0.25);
    font-family: "Cinzel", serif;
    overflow: hidden;
  }
  .brand {
    position: absolute;
    left: 250px;
    top: 120px;
    display: flex;
    align-items: center;
    gap: 26px;
  }
  .brand-circle {
    width: 130px;
    height: 130px;
    border: 6px solid var(--brand-red);
    border-radius: 50%;
    box-sizing: border-box;
  }
  .brand-name {
    color: var(--brand-red);
    font-size: 46px;
    font-weight: 400;
    letter-spacing: 1px;
    white-space: nowrap;
    margin-top: 40px;
  }
  .name-band {
    position: absolute;
    left: 0;
    top: 320px;
    width: 100%;
    height: 76px;
    background: var(--band-red);
    border-top: 5px solid var(--band-edge);
    border-bottom: 5px solid var(--band-edge);
    box-sizing: border-box;
    box-shadow: 0 -12px 0 -6px var(--band-red), 0 12px 0 -6px var(--band-red);
  }
  .person-name {
    position: absolute;
    left: 300px;
    top: 0;
    line-height: 66px;
    color: var(--text-light);
    font-size: 26px;
    letter-spacing: 0.5px;
  }
  .contact-list {
    position: absolute;
    left: 115px;
    top: 448px;
    margin: 0;
    padding: 0;
    list-style: none;
    color: var(--text-muted);
    font-size: 15px;
    letter-spacing: 0.4px;
  }
  .contact-row {
    display: flex;
    gap: 18px;
    margin-bottom: 14px;
  }
  .contact-item {
    display: flex;
    align-items: center;
    gap: 7px;
    white-space: nowrap;
  }
  .contact-dot {
    width: 10px;
    height: 10px;
    border-radius: 50%;
    background: var(--brand-red);
    flex: none;
  }
</style>
</head>
<body>
<div class="canvas">
  <section class="business-card">
    <div class="brand">
      <div class="brand-circle"></div>
      <div class="brand-name">R &amp; T Auto Body</div>
    </div>

    <div class="name-band">
      <div class="person-name">Delmor Quenivash</div>
    </div>

    <ul class="contact-list">
      <li class="contact-row">
        <span class="contact-item"><span class="contact-dot"></span>28476 Pellway Street Corvale, CA 90999</span>
        <span class="contact-item"><span class="contact-dot"></span>555-014-3381</span>
        <span class="contact-item"><span class="contact-dot"></span>555-019-6624</span>
      </li>
      <li class="contact-row">
        <span class="contact-item"><span class="contact-dot"></span>555-017-4092</span>
        <span class="contact-item"><span class="contact-dot"></span>rtautobodyinc@brivomail.com</span>
        <span class="contact-item"><span class="contact-dot"></span>www.rtautobody-example.com</span>
      </li>
    </ul>
  </section>
</div>
</body>
</html>
```